Crestline Lending Group Business Cards

We are looking to revamp the current business cards each of our locations uses. We are a lending company that specializes in personal loans, title loans, and tax services. We have locations in New Mexico, Texas, and Oklahoma.

We would like a cleaner, sleeker look while still highlighting what we offer. Title Loans, Personal Loans & Tax Services. We also want to include our referral fee somewhere on the card. We would like to see an English option as well as a Spanish option for the cards.

PLEASE NOTE: Some business cards do not include the employee's name but just the store's location, while others will include both.

These are double-sided business cards, and we would like to see proof if possible. I have included proofs of our current business cards for you to review below, as well as our company logo. Feel free to get creative with the logo, etc! Colors should match the logo; however, you do not need to use all of our logo colors if you don't want to.

```html
<!DOCTYPE html>
<html lang="en">
<head>
<meta charset="utf-8">
<title>Crestline Lending Group Business Card</title>
<link href="https://fonts.googleapis.com/css2?family=Francois+One&family=Montserrat:wght@400&display=swap" rel="stylesheet">
<style>
  :root {
    --green: #0f5a2e;
    --red: #c8202b;
    --white: #ffffff;
    --page: #f1f1f1;
  }
  * { box-sizing: border-box; margin: 0; padding: 0; }
  html, body { width: 1200px; height: 1200px; overflow: hidden; }
  body {
    background: var(--page);
    font-family: "Francois One", "Arial Narrow", sans-serif;
    display: flex;
    flex-direction: column;
    align-items: center;
    justify-content: center;
    gap: 60px;
  }
  .card {
    width: 900px;
    height: 502px;
    background: var(--white);
    position: relative;
    box-shadow: 0 6px 18px rgba(0,0,0,.12);
    overflow: hidden;
  }

  /* Front */
  .front-top { position: absolute; top: 0; left: 0; right: 0; height: 328px; display: flex; }
  .brand-panel {
    width: 279px; display: flex; align-items: center; justify-content: center; gap: 10px;
  }
  .brand-panel.right { width: 281px; }
  .brand-dot { width: 14px; height: 14px; border-radius: 50%; background: var(--red); flex: none; }
  .brand-name {
    color: var(--green); font-size: 30px; line-height: 1.05; text-align: left;
  }
  .contact-panel {
    width: 340px; background: var(--green); color: var(--white);
    display: flex; flex-direction: column; align-items: center; justify-content: center; text-align: center;
  }
  .contact-name { font-size: 46px; line-height: 1; }
  .contact-title {
    font-family: "Montserrat", sans-serif; font-weight: 400; font-size: 22px; letter-spacing: .5px; margin-top: 2px;
  }
  .contact-phone { font-size: 46px; line-height: 1.1; margin-top: 8px; }
  .contact-email { font-size: 27px; line-height: 1.1; }
  .services {
    position: absolute; top: 328px; left: 0; right: 0; height: 83px; background: var(--red);
    display: flex; align-items: center; justify-content: space-evenly; color: var(--white); font-size: 33px;
  }
  .service { display: flex; align-items: center; gap: 12px; }
  .service::before {
    content: ""; width: 18px; height: 18px; border-radius: 50%; background: var(--green);
  }
  .address {
    position: absolute; top: 411px; left: 0; right: 0; height: 91px;
    display: flex; align-items: center; justify-content: center; color: var(--green); font-size: 38px;
  }

  /* Back */
  .back-band {
    position: absolute; left: 0; right: 0; height: 136px; background: var(--green);
    display: flex; align-items: center; justify-content: center; gap: 22px; color: var(--white);
  }
  .back-band.top { top: 0; font-size: 42px; }
  .back-band.bottom { bottom: 0; font-size: 42px; }
  .rule { width: 210px; height: 5px; background: var(--white); }
  .offer {
    position: absolute; top: 136px; left: 0; right: 0; height: 230px;
    display: flex; align-items: center; justify-content: center; gap: 18px; color: var(--green);
  }
  .offer-big { font-size: 200px; line-height: 1; letter-spacing: -2px; }
  .offer-small {
    color: var(--red); font-size: 86px; line-height: .92; display: flex; flex-direction: column; align-items: center;
  }
</style>
</head>
<body>
  <section class="card card-front">
    <div class="front-top">
      <div class="brand-panel">
        <span class="brand-dot"></span>
        <span class="brand-name">Crestline<br>Lending Group</span>
      </div>
      <div class="contact-panel">
        <div class="contact-name">Jane Doe</div>
        <div class="contact-title">BRANCH MANAGER</div>
        <div class="contact-phone">(505) 555-1212</div>
        <div class="contact-email">abcde@crestlinelending.com</div>
      </div>
      <div class="brand-panel right">
        <span class="brand-dot"></span>
        <span class="brand-name">Crestline<br>Lending Group</span>
      </div>
    </div>
    <div class="services">
      <span class="service">TITLE LOANS</span>
      <span class="service">PERSONAL LOANS</span>
      <span class="service">TAX SERVICES</span>
    </div>
    <div class="address">123 Elm Street, Suite B, Anytown, Texas 55555</div>
  </section>

  <section class="card card-back">
    <div class="back-band top">
      <span class="rule"></span><span>Refer a Friend</span><span class="rule"></span>
    </div>
    <div class="offer">
      <span class="offer-big">GET</span>
      <span class="offer-small"><span>UP</span><span>TO</span></span>
      <span class="offer-big">$100</span>
    </div>
    <div class="back-band bottom">
      <span class="rule"></span><span>www.crestlinelending.com</span><span class="rule"></span>
    </div>
  </section>
</body>
</html>
```